Modern Billboard Ad for Criminal Defense Firm

10.5 x 36 We're looking for something to set us apart from the local competition. Looking for sleek and modern. We're a mid-sized firm in a small market city. We want to give the artist room to be creative on this one.
Thanks

Target Market(s)

Adult clients who have been charged with a crime/DWI

Industry/Entity Type

legal

Font styles to use
Serif
Sans Serif

Requirements
Must have
• Needs to have the firm name in large lettering. Law Offices of Marcus T Whitfield. “PLLC” does not have to be included. Phone number of (555) 384-1927 should be included but not the main focus.
Nice to have
• A call to action or something similar. “Don’t go it alone, call today.”, “ Arrested?”

```html
<!DOCTYPE html>
<html lang="en">
<head>
<meta charset="utf-8">
<title>Marcus T Whitfield – Billboard</title>
<link rel="stylesheet" href="https://fonts.googleapis.com/css2?family=Tinos:wght@400;700&family=Montserrat:wght@700;800;900&display=swap">
<style>
  :root {
    --page-bg: #e9ebef;
    --header-bg: #ffffff;
    --ink: #111111;
    --firm-blue: #1d4fa6;
    --navy-deep: #0b1633;
    --navy: #15307a;
    --royal: #1f47a8;
    --gold-top: #ffd21f;
    --gold-bottom: #f5a900;
    --gold: #ffc20e;
    --white: #ffffff;
    --shadow: #0a1430;
  }
  * { margin: 0; padding: 0; box-sizing: border-box; }
  html, body { width: 1200px; height: 768px; overflow: hidden; background: var(--page-bg); }
  .billboard {
    position: absolute; left: 20px; top: 214px;
    width: 1160px; height: 340px;
    overflow: hidden;
    box-shadow: 0 10px 30px rgba(10, 20, 48, .25);
  }
  .firm-header {
    height: 88px; background: var(--header-bg);
    display: flex; align-items: center; justify-content: center;
    font-family: "Tinos", "Times New Roman", serif;
    font-size: 52px; line-height: 1; white-space: nowrap;
  }
  .firm-header .prefix { color: var(--ink); font-weight: 400; margin-right: 14px; }
  .firm-header .name { color: var(--firm-blue); font-weight: 700; }
  .ad-panel { position: relative; height: 252px; background: var(--navy-deep); }
  .ad-panel .backdrop { position: absolute; inset: 0; width: 100%; height: 100%; }
  .client-photo {
    position: absolute; left: 0; top: 0; width: 330px; height: 252px;
    background: radial-gradient(ellipse at 55% 60%, #c9a58e 0%, #8a6a58 30%, #2a2523 60%, #050505 85%);
  }
  .headline {
    position: absolute; left: 330px; top: 12px; width: 715px; text-align: center;
    font-family: "Montserrat", Arial, sans-serif; font-weight: 900;
    font-size: 106px; line-height: 1; letter-spacing: -1px;
    background: linear-gradient(180deg, var(--gold-top) 0%, var(--gold-bottom) 100%);
    -webkit-background-clip: text; background-clip: text; color: transparent;
    filter: drop-shadow(4px 5px 0 var(--shadow));
  }
  .call-to-action {
    position: absolute; left: 330px; top: 136px; width: 630px; text-align: center;
    font-family: "Montserrat", Arial, sans-serif; font-weight: 800;
    font-size: 31px; color: var(--white); letter-spacing: .3px;
    text-shadow: 2px 2px 0 var(--shadow);
  }
  .phone {
    position: absolute; left: 330px; top: 176px; width: 630px; text-align: center;
    font-family: "Montserrat", Arial, sans-serif; font-weight: 800;
    font-size: 50px; color: var(--white); line-height: 1.1;
    text-shadow: 3px 3px 0 var(--shadow);
  }
  .attorney-portrait {
    position: absolute; left: 970px; top: 130px; width: 84px; height: 98px;
    border: 2px solid var(--white);
    background: linear-gradient(180deg, #6b5a48 0%, #8d7a6a 40%, #3d4a60 100%);
  }
  .award-badge {
    position: absolute; left: 1066px; top: 130px; width: 68px; height: 98px;
    border: 2px solid var(--white);
    background: linear-gradient(180deg, #3fa8e0 0%, #3fa8e0 12%, #1a1a1a 12%, #1a1a1a 85%, #3fa8e0 85%);
  }
</style>
</head>
<body>
  <main class="billboard">
    <header class="firm-header">
      <span class="prefix">LAW OFFICES OF</span><span class="name">MARCUS T WHITFIELD</span>
    </header>
    <section class="ad-panel">
      <svg class="backdrop" viewBox="0 0 1160 252" preserveAspectRatio="none" aria-hidden="true">
        <defs>
          <linearGradient id="panelBlue" x1="0" y1="0" x2="1" y2="0">
            <stop offset="0" stop-color="#050a1c"/>
            <stop offset=".35" stop-color="#0d1f55"/>
            <stop offset=".7" stop-color="#1a3d95"/>
            <stop offset="1" stop-color="#143381"/>
          </linearGradient>
        </defs>
        <rect width="1160" height="252" fill="url(#panelBlue)"/>
        <polygon points="760,0 1010,0 860,252 610,252" fill="#2450b5" opacity=".25"/>
        <polygon points="1040,0 1160,0 1160,40 1000,252 930,252" fill="#2a58c2" opacity=".3"/>
        <line x1="1160" y1="100" x2="1050" y2="252" stroke="#ffc20e" stroke-width="2"/>
        <polygon points="1160,120 1160,252 1070,252" fill="#ffc20e"/>
      </svg>
      <div class="client-photo" role="img" aria-label="Photo of a distressed man in handcuffs raising his fists"></div>
      <h1 class="headline">ARRESTED?</h1>
      <p class="call-to-action">DON’T GO IT ALONE, CALL TODAY</p>
      <p class="phone">(555) 384-1927</p>
      <div class="attorney-portrait" role="img" aria-label="Portrait photo of the attorney in a suit"></div>
      <div class="award-badge" role="img" aria-label="Local best-of award badge"></div>
    </section>
  </main>
</body>
</html>
```